| 希望する色 | 黄系 |
■概要 復刻発売する「そよかぜカステラ」のパッケージデザインを広く募集いたします ■依頼概要 私たち森灯舎は、千葉県君津市で「はちみつを五感で楽しむ」をコンセプトに「こもれびとワインのもりあかり舎」という観光施設を運営している会社です。 今回募集するのは店舗で復刻発売する「そよかぜカステラ」のパッケージデザインです。 ※自社ホームページ(http://moriakari-sha.example/) 商品名 そよかぜカステラ 商品販売価格 5切入:680-780円(仮) ターゲット 30~40代女性、ファミリー層、50~70代男女 コンセプト 「思わず微笑んでしまう、どこか懐かしいおいしさ」 当店は地元のお客様だけではなく、遠方からも個人のお客様、バスツアーの立ち寄り場所として多くのお客様にご来店いただいております。 そのため、当店をお選び下さったお客様が楽しんでいただけるような「蜂蜜採取体験ツアー」や「蜂蜜の食べ比べ」など数多くの取り組みを行っています。 そよかぜカステラは、店舗が移転をする 約6年前より もりあかり舎の人気商品として販売をしておりました。 常連のお客様からは「あのカステラはなくなってしまったの?」「復活してほしいなぁ」等 多数お声が寄せられていた、待望の復刻商品です。 デザインイメージ 蜂蜜を扱う会社の自社製造商品ですので、「はちみつ」「はちみつ屋さん」「養蜂家」等のワードが連想できるイラストや構成でお願いします。 どの層のお客様でも思わず手に取ってしまうような、目を引くようなデザインを募集しています。 細かな指定はございませんので、コンセプトに合うものを自由にご提案ください。 ※ 「復刻商品」「懐かしい商品」ということに捕らわれず、幅広くデザインをご提案いただけますと幸いです。 味の特徴 卵とはちみつの味がやさしく香る、どこかなつかしい味わいのカステラです。 ふんわり もちっとした生地との相性も抜群。どの年齢のお客さまからも愛される商品を目指しました。 応募方法 ・ラベルのデザイン方法 ・ ご提案いただく際ですが、添付のような展開図でご提案いただけますと幸いでございます。 ・ 細かなサイズはデザイン決定後に打ち合わせをしたく存じます ・ 成分表示や製造元などの詳細記載欄は デザイン決定後に打ち合わせをしたく存じます。提案時は 空欄もしくは仮置きでお願いいたします ■納品ファイル形式 ------------------- ・編集可能なファイル形式(ai) ・確認用(JPG,PDFなど) 沢山のご応募をスタッフ一同お待ちしております!! ■報酬 ------------------ ・100,000円 ※納品物の著作権は弊社に譲渡いただき、 著作者人格権を行使しないことにご同意の上ご応募ください ※報酬金額(税込)からシステム利用料を差し引いた金額が、ワーカーさまの受取金額となります ■禁止事項 ------------------ ※他で登録されているデザインの転用 ※他のクライアントへ提出した内容の転用 その他、ご不明点はお問い合わせください。 イメージ通りデザインにするため 皆さまからのご提案をお待ちしております。 よろしくお願いいたします! その他ご質問等ありましたら、気軽にお問い合わせください。 ご応募をお待ちしております! |
採用させていただきました理由としましては
デザインを拝見した際に 現状の他商品のパッケージとのなじみ・親和性が非常に高いという印象を受けました。
しかし、ただなじみが良いだけでなく、単体としてのデザイン性の高さ
洗練されていて 高級感もあり、あたたかみもある絶妙なデザインバランスが
我々がそよかぜカステラに求めるイメージとうまく合致いたしまして、デザインを決定いたしました。
この度も多くのクリエイター様に沢山のご応募そしてご提案いただきましたこと
心より感謝申し上げます。
また当社コンペに何度もご応募していただいているクリエイター様、
初めてチャレンジしようと思って応募して下さったクリエイター様、
なにより私共では完成できない商品のデザインという部分で、
本当に多くの皆様に助けていただきましたこと感謝してもしきれません。
誠にありがとうございました。
ご応募くださった皆様のデザイン一つ一つ拝見させていただき、
皆様がそれぞれ様々な思いをもってご応募くださっている気持ち
スタッフ一同伝わってまいりました。
メッセージを多数いただき、お返事をできかねているクリエイター様には
お時間を頂戴し誠に申し訳ございませんが、随時メッセージを送らせていただきたく存じます。
この度は当社として思い入れのある 復刻の商品ということもあり、
非常に難しい募集案件ではあったかと存じますが、
そのこだわりをお客様にも感じていただきたいと願っております。
多くの皆様にお力添えいただきました商品を、
スタッフ一同販売促進にも力を入れて、
皆様のお手元に届くような商品になっていけるよう頑張ってまいりたいと思います。
また、新商品が出た際にはこちらできた墓集をかけさせていただくと思いますので、
その際は是非お力添えをいただけますと幸いです。
重ねてとなりますが、この度も素敵な素晴らしいデザインのご提案をいただき、誠にありがとうございます。
今後とも株式会社森灯舎をよろしくお願いいたします。

```html
<!DOCTYPE html>
<html lang="ja">
<head>
<meta charset="utf-8">
<title>そよかぜカステラ パッケージ展開図</title>
<link rel="stylesheet" href="https://fonts.googleapis.com/css2?family=Zen+Maru+Gothic:wght@500;700&family=Noto+Sans+JP:wght@400;500&display=swap">
<style>
  :root {
    --paper: #ffffff;
    --gold: #c9961f;
    --gold-deep: #b3821a;
    --gold-soft: #e8c456;
    --check-pale: #fbf2b8;
    --check-warm: #f0d25c;
    --label-cream: #fff7cf;
    --label-edge: #f3dc78;
    --brown: #5e3518;
    --slice-top: #6b3a1e;
    --slice-body: #f2cf4a;
    --crop: #9a9a9a;
    --fold: #a87a14;
  }
  html, body {
    margin: 0;
    padding: 0;
    width: 1200px;
    height: 1120px;
    overflow: hidden;
    background: var(--paper);
  }
  .dieline {
    display: block;
    width: 1200px;
    height: 1120px;
  }
  .flap, .panel-base { fill: var(--gold); }
  .fold-line { stroke: var(--fold); stroke-width: 0.4; stroke-dasharray: 2 1.5; fill: none; }
  .crop-mark { stroke: var(--crop); stroke-width: 0.35; fill: none; }
  .label-frame { fill: var(--gold-deep); }
  .label-edge { fill: var(--label-edge); }
  .label-face { fill: var(--label-cream); }
  .label-corner { fill: var(--gold-soft); }
  .product-kicker {
    font-family: "Zen Maru Gothic", sans-serif;
    font-weight: 700;
    font-size: 11px;
    fill: var(--brown);
    letter-spacing: 0.5px;
  }
  .product-name {
    font-family: "Zen Maru Gothic", sans-serif;
    font-weight: 700;
    font-size: 27px;
    fill: var(--brown);
    letter-spacing: 0.5px;
  }
  .nutrition-text {
    font-family: "Noto Sans JP", sans-serif;
    font-weight: 500;
    font-size: 4.4px;
    fill: var(--brown);
  }
  .nutrition-rule { stroke: var(--brown); stroke-width: 0.3; }
  .recycle-mark { fill: none; stroke: var(--brown); stroke-width: 0.6; }
</style>
</head>
<body>
<svg class="dieline" viewBox="0 0 480 448" xmlns="http://www.w3.org/2000/svg" aria-label="そよかぜカステラ 箱の展開図">
  <defs>
    <linearGradient id="check-fill" x1="0" y1="0" x2="1" y2="1">
      <stop offset="0" stop-color="var(--check-pale)"/>
      <stop offset="0.5" stop-color="var(--check-warm)"/>
      <stop offset="1" stop-color="var(--check-pale)"/>
    </linearGradient>
    <linearGradient id="slice-fill" x1="0" y1="0" x2="0" y2="1">
      <stop offset="0" stop-color="var(--slice-top)"/>
      <stop offset="0.2" stop-color="var(--slice-top)"/>
      <stop offset="0.22" stop-color="var(--slice-body)"/>
      <stop offset="1" stop-color="var(--slice-body)"/>
    </linearGradient>
  </defs>

  <!-- crop marks -->
  <g class="crop-marks">
    <path class="crop-mark" d="M6,14 H22 M14,6 V22"/>
    <circle class="crop-mark" cx="14" cy="14" r="3"/>
    <path class="crop-mark" d="M458,14 H474 M466,6 V22"/>
    <circle class="crop-mark" cx="466" cy="14" r="3"/>
    <path class="crop-mark" d="M6,434 H22 M14,426 V442"/>
    <circle class="crop-mark" cx="14" cy="434" r="3"/>
    <path class="crop-mark" d="M458,434 H474 M466,426 V442"/>
    <circle class="crop-mark" cx="466" cy="434" r="3"/>
    <path class="crop-mark" d="M232,4 V16 M226,10 H238"/>
    <path class="crop-mark" d="M232,432 V444 M226,438 H238"/>
  </g>

  <!-- top tuck flap and dust flaps -->
  <g class="top-flaps">
    <path class="flap" d="M255,130 V45 Q255,30 270,30 H363 Q378,30 378,45 V130 Z"/>
    <path class="flap" d="M205,130 L209,96 Q211,88 219,88 H255 V130 Z"/>
    <path class="flap" d="M428,130 L424,96 Q422,88 414,88 H378 V130 Z"/>
    <path class="fold-line" d="M255,85 H378"/>
  </g>

  <!-- main body -->
  <g class="body-panels">
    <path class="flap" d="M33,140 L55,130 V318 L33,308 Z"/>
    <rect class="panel-base" x="55" y="130" width="405" height="188"/>
    <rect x="55" y="130" width="405" height="188" fill="url(#check-fill)" role="img" aria-label="淡い黄色と濃い黄色の市松模様"/>
    <path class="fold-line" d="M55,130 V318 M170,130 V318 M255,130 V318 M378,130 V318 M55,130 H460 M55,318 H460"/>
  </g>

  <!-- bottom flap and dust flaps -->
  <g class="bottom-flaps">
    <path class="flap" d="M255,318 V405 Q255,420 270,420 H363 Q378,420 378,405 V318 Z"/>
    <path class="flap" d="M205,318 H255 V360 H219 Q211,360 209,352 Z"/>
    <path class="flap" d="M428,318 H378 V360 H414 Q422,360 424,352 Z"/>
  </g>

  <!-- front label -->
  <g class="front-label">
    <rect class="label-frame" x="258" y="137" width="117" height="176"/>
    <rect class="label-edge" x="265" y="144" width="103" height="162"/>
    <rect class="label-face" x="270" y="149" width="93" height="152"/>
    <polygon class="label-corner" points="270,149 363,149 316.5,163"/>
    <polygon class="label-corner" points="270,301 363,301 316.5,287"/>
    <circle cx="316.5" cy="136" r="5" fill="var(--brown)" role="img" aria-label="八角の飾り"/>
    <circle cx="316.5" cy="299" r="5" fill="var(--brown)" role="img" aria-label="八角の飾り"/>
    <circle cx="305" cy="163" r="7" fill="var(--brown)" role="img" aria-label="ミツバチのイラスト"/>
    <text class="product-kicker" x="316.5" y="190" text-anchor="middle">そよかぜ</text>
    <text class="product-name" x="316.5" y="224" text-anchor="middle">カステラ</text>
    <rect x="289" y="237" width="44" height="40" fill="url(#slice-fill)" role="img" aria-label="切り分けたカステラのイラスト"/>
  </g>

  <!-- nutrition facts on side panel -->
  <g class="nutrition">
    <text class="nutrition-text" x="62" y="272">栄養成分表示（1切あたり）</text>
    <line class="nutrition-rule" x1="62" y1="274" x2="126" y2="274"/>
    <text class="nutrition-text" x="62" y="280">エネルギー</text><text class="nutrition-text" x="103" y="280">129kcal</text>
    <text class="nutrition-text" x="62" y="286">たんぱく質</text><text class="nutrition-text" x="103" y="286">3.4g</text>
    <text class="nutrition-text" x="62" y="292">脂　　質</text><text class="nutrition-text" x="103" y="292">3.1g</text>
    <text class="nutrition-text" x="62" y="298">炭水化物</text><text class="nutrition-text" x="103" y="298">21.4g</text>
    <text class="nutrition-text" x="62" y="304">食塩相当量</text><text class="nutrition-text" x="103" y="304">0.04g</text>
    <text class="nutrition-text" x="104" y="310">（推定値）</text>
    <circle class="recycle-mark" cx="150" cy="296" r="3.5"/>
  </g>
</svg>
</body>
</html>
```